I need a business card design for my new clinic (SPORTS MEDICINE OF KNEE). I am orthopedist, expert in sports surgery, especially knee surgery. I prefer, as colors, the colors of my logo (green, black and white). I already have my logo and should appear on my card. It's good to see my site to have ideas (www.drlucianovarela.com)
It needs contain:
my name: Dr. Luciano Varela
my registration: CRM 584-902
my specialty: Cirurgia do Joelho / Esporte
my address: Centro Executivo - Pinheiral Plaza
Av. Doutor Augusto Brandão Cunha, 2740 sala 0836
Jd. Ipanema - Ribeirão Preto - SP
my phone number: Tel (16) 8245-3908
my clinic phone: (16) 3670-4851
my e-mail: drlucianovarela@mailbox-exemplo.com
my site: www.drlucianovarela.com

Target Market(s)

futures patients

Industry/Entity Type

Clinic

Requirements
Nice to have
• letters not overfilled
straight lines, with few curves

```html
<!DOCTYPE html>
<html lang="pt-BR">
<head>
<meta charset="UTF-8">
<title>Varela – Cartão de Visita</title>
<link rel="stylesheet" href="https://fonts.googleapis.com/css2?family=Roboto+Condensed:wght@300;400&display=swap">
<style>
  :root{
    --bg:#e9e4dc;
    --paper:#ffffff;
    --green:#2f8f58;
    --green-dark:#217a46;
    --green-light:#4fbf7c;
    --green-text:#35a15f;
    --ink:#111111;
    --white:#ffffff;
  }
  *{margin:0;padding:0;box-sizing:border-box;}
  html,body{width:1200px;height:743px;overflow:hidden;background:var(--bg);}
  .canvas{position:relative;width:1200px;height:743px;}

  .card{position:absolute;width:540px;height:320px;background:var(--paper);overflow:hidden;box-shadow:0 6px 18px rgba(0,0,0,.18);}

  .brand{display:flex;align-items:center;gap:12px;}
  .brand-mark{width:36px;height:36px;background:var(--ink);}
  .brand-name{font-family:"Roboto Condensed",sans-serif;font-weight:400;font-size:42px;color:var(--ink);letter-spacing:2px;line-height:1;}

  /* front */
  .card-front{left:70px;top:50px;}
  .card-front .brand{position:absolute;left:40px;top:66px;}
  .doctor{position:absolute;right:30px;top:38px;text-align:right;font-family:"Roboto Condensed",sans-serif;font-weight:300;color:var(--green-text);font-size:17px;line-height:27px;}
  .band{position:absolute;left:0;bottom:0;width:100%;height:160px;}
  .band svg{display:block;}
  .contact,.address{position:absolute;font-family:"Roboto Condensed",sans-serif;font-weight:300;color:var(--white);font-size:13.5px;line-height:17px;}
  .contact{left:40px;bottom:26px;}
  .address{right:30px;bottom:50px;text-align:right;}

  /* back */
  .card-back{left:590px;top:380px;}
  .card-back .brand{position:absolute;left:40px;top:80px;}
  .edge{position:absolute;right:0;top:0;}
  .site-bar{position:absolute;left:0;bottom:50px;width:470px;height:30px;background:var(--ink);display:flex;align-items:center;justify-content:center;}
  .site{font-family:"Roboto Condensed",sans-serif;font-weight:400;color:var(--green-light);font-size:18px;letter-spacing:9px;}
</style>
</head>
<body>
<main class="canvas">

  <section class="card card-front" aria-label="Frente do cartão">
    <div class="brand">
      <span class="brand-mark"></span>
      <span class="brand-name">VARELA</span>
    </div>
    <div class="doctor">
      <p>Dr. Luciano Varela</p>
      <p>CRM 584-902</p>
      <p>Cirurgia do Joelho / Esporte</p>
    </div>
    <div class="band">
      <svg width="540" height="160" viewBox="0 0 540 160">
        <defs>
          <linearGradient id="sheen" x1="0" y1="0" x2="1" y2="0">
            <stop offset="0" stop-color="#7fe0a6" stop-opacity="0"/>
            <stop offset="0.5" stop-color="#7fe0a6" stop-opacity=".55"/>
            <stop offset="1" stop-color="#7fe0a6" stop-opacity="0"/>
          </linearGradient>
        </defs>
        <rect width="540" height="160" fill="var(--green)"/>
        <polygon points="0,160 0,40 540,0 540,160" fill="var(--green-dark)" opacity=".35"/>
        <rect x="60" y="18" width="420" height="4" fill="url(#sheen)" transform="rotate(-4 270 20)"/>
      </svg>
    </div>
    <div class="contact">
      <p>Tel (16) 8245-3908</p>
      <p>Clinic phone: (16) 3670-4851</p>
      <p>E-mail: drlucianovarela@mailbox-exemplo.com</p>
    </div>
    <div class="address">
      <p>Centro Executivo - Pinheiral Plaza</p>
      <p>Av. Doutor Augusto Brandão Cunha,</p>
      <p>2740 sala 0836</p>
      <p>Jd. Ipanema - Ribeirão Preto - SP</p>
    </div>
  </section>

  <section class="card card-back" aria-label="Verso do cartão">
    <svg class="edge" width="70" height="320" viewBox="0 0 70 320">
      <rect x="58" y="0" width="12" height="320" fill="var(--ink)"/>
      <path d="M20 0 H58 V40 A38 38 0 0 1 20 0 Z" fill="var(--green-light)"/>
      <path d="M58 100 A40 40 0 0 0 18 140 V260 H58 Z" fill="var(--green-light)"/>
    </svg>
    <div class="brand">
      <span class="brand-mark"></span>
      <span class="brand-name">VARELA</span>
    </div>
    <div class="site-bar">
      <span class="site">www.drlucianovarela.com</span>
    </div>
  </section>

</main>
</body>
</html>
```